The Ledgerline Business Card

Business card with QR Code for an accounting and tax business

Target Market(s)

Small Business and Individual Tax

Industry/Entity Type

Bookkeeping, Accounting and Taxes

Contact Information for Business Card

482 CALDWELL ST STE 2210 #614273 BOSTON, MA Zip: 02387

Requirements
Must have
• Name and Address

```html
<!DOCTYPE html>
<html lang="en">
<head>
<meta charset="utf-8">
<title>The Ledgerline Business Card</title>
<link rel="stylesheet" href="https://fonts.googleapis.com/css2?family=Cinzel:wght@600;700&family=Arimo:wght@400&display=swap">
<style>
  :root {
    --stage: #3a3a3c;
    --card: #232325;
    --ink: #f2f2f2;
    --ink-soft: #cfcfd1;
    --rule: #8a8a8d;
  }
  * { margin: 0; padding: 0; box-sizing: border-box; }
  html, body { width: 1200px; height: 689px; overflow: hidden; background: var(--stage); }
  .canvas { position: relative; width: 1200px; height: 689px; background: var(--stage); }
  .card {
    position: absolute; top: 190px; width: 540px; height: 309px;
    background: var(--card); border-radius: 18px; color: var(--ink);
  }
  .card--front { left: 40px; display: flex; align-items: center; justify-content: center; }
  .card--back { left: 620px; }

  .brand { display: flex; align-items: center; gap: 14px; font-family: "Cinzel", serif; font-weight: 700; color: var(--ink); }
  .brand__dot { border: 3px solid var(--ink); border-radius: 50%; flex: none; }
  .card--front .brand { font-size: 30px; letter-spacing: 1px; }
  .card--front .brand__dot { width: 56px; height: 56px; }

  .back__brand { position: absolute; left: 34px; top: 0; bottom: 0; width: 250px; display: flex; align-items: center; justify-content: center; }
  .card--back .brand { flex-direction: column; gap: 10px; font-size: 22px; letter-spacing: 0.5px; }
  .card--back .brand__dot { width: 46px; height: 46px; border-width: 2.5px; }

  .back__rule { position: absolute; left: 300px; top: 40px; bottom: 40px; width: 1px; background: linear-gradient(var(--card), var(--rule) 30%, var(--rule) 70%, var(--card)); }

  .contact { position: absolute; left: 322px; top: 58px; font-family: "Arimo", sans-serif; font-size: 12px; line-height: 1.4; color: var(--ink-soft); }
  .contact__name { font-family: "Cinzel", serif; font-weight: 700; font-size: 17px; color: var(--ink); letter-spacing: 0.5px; }
  .contact__title { margin-bottom: 18px; font-size: 11px; }
  .contact__address { margin-bottom: 18px; }
  .contact__list { list-style: none; }
  .contact__list li { display: flex; align-items: center; gap: 8px; }
  .contact__list svg { width: 10px; height: 10px; fill: var(--ink-soft); flex: none; }
</style>
</head>
<body>
<div class="canvas">
  <section class="card card--front">
    <div class="brand"><span class="brand__dot"></span><span>The Ledgerline</span></div>
  </section>

  <section class="card card--back">
    <div class="back__brand">
      <div class="brand"><span class="brand__dot"></span><span>The Ledgerline</span></div>
    </div>
    <div class="back__rule"></div>
    <div class="contact">
      <p class="contact__name">DANIEL HARTWELL</p>
      <p class="contact__title">Managing Director</p>
      <p class="contact__address">482 Caldwell St Ste 2210<br>#614273 Boston, MA Zip: 02387</p>
      <ul class="contact__list">
        <li><svg viewBox="0 0 10 10"><path d="M2 0.5l2 2-1 1.2c.6 1.3 1.6 2.3 2.9 2.9l1.2-1 2 2-1.2 1.6C4.4 8.8 1.2 5.6.4 1.7z"/></svg>555-214-7730</li>
        <li><svg viewBox="0 0 10 10"><path d="M2.5 0h5v10h-5zM3.3 1v7h3.4V1z"/></svg>555-382-9061</li>
        <li><svg viewBox="0 0 10 10"><path d="M0 2h10v6H0zM1 3v.3l4 2.6 4-2.6V3z"/></svg>info@theledgerline.com</li>
        <li><svg viewBox="0 0 10 10"><path d="M5 0a5 5 0 110 10A5 5 0 015 0zm0 1.2a3.8 3.8 0 100 7.6 3.8 3.8 0 000-7.6z"/></svg>www.theledgerline.com</li>
      </ul>
    </div>
  </section>
</div>
</body>
</html>
```